Building Company Business Card Design

Need a design for a business card:
It needs to have: Name, Phone, Facebook link, Website, email
i would also like a list of works we undertake:
-New Homes
-Extensions, Renovations & Bathrooms
-Decking, Carports, Sheds (Residential and Industrial)
-Carpentry
-Fences, Patios & Pergolas

Name, Phone, Facebook link, Website, email + details of services provided listed in description

```html
<!DOCTYPE html>
<html lang="en">
<head>
<meta charset="utf-8">
<title>Keystone Homes – Business Card</title>
<link href="https://fonts.googleapis.com/css2?family=Michroma&family=Lato:wght@400;700&display=swap" rel="stylesheet">
<style>
  :root {
    --stage: #2e2e2e;
    --card-black: #0b0b0b;
    --pattern-dark: #161616;
    --pattern-mid: #232323;
    --brand-green: #33b54d;
    --brand-grey: #8a8a8a;
    --brand-light: #d9d9d9;
    --white: #ffffff;
    --muted: #e6e6e6;
  }
  * { box-sizing: border-box; margin: 0; padding: 0; }
  html, body {
    width: 1200px; height: 689px; overflow: hidden;
    background: var(--stage);
    font-family: "Lato", Arial, sans-serif;
  }
  .canvas {
    position: relative; width: 1200px; height: 689px;
    display: flex; align-items: center; justify-content: center; gap: 40px;
  }
  .card {
    position: relative; width: 540px; height: 309px;
    border-radius: 18px; overflow: hidden;
    background: var(--card-black);
    box-shadow: 0 18px 40px rgba(0,0,0,.45);
  }

  /* Back of card */
  .card-back .pattern-field {
    position: absolute; inset: 0;
    background: linear-gradient(135deg, var(--pattern-mid), var(--pattern-dark) 60%, var(--card-black));
  }
  .card-back .brand-tag {
    position: absolute; top: 78px; left: 0; right: 0;
    display: flex; align-items: center; justify-content: center; gap: 10px;
    font-family: "Lato", Arial, sans-serif; font-weight: 700;
    font-size: 22px; letter-spacing: 4px; color: var(--brand-green);
  }
  .brand-tag .brand-square {
    width: 18px; height: 18px; background: var(--brand-green);
  }
  .services {
    position: absolute; top: 140px; left: 0; right: 0;
    list-style: none; text-align: center;
    font-family: "Michroma", Arial, sans-serif; font-size: 12.5px;
    line-height: 28px; color: var(--white);
  }
  .services .bullet { color: var(--brand-green); margin: 0 6px; }

  /* Front of card */
  .front-mark {
    position: absolute; top: 0; right: 0; width: 230px; height: 100%;
    clip-path: polygon(0 0, 100% 0, 100% 100%, 28% 100%);
    background: linear-gradient(160deg, var(--brand-green) 0 45%, var(--brand-light) 45% 55%, var(--brand-grey) 55%);
  }
  .front-content { position: absolute; left: 34px; top: 36px; width: 320px; }
  .company-name {
    font-family: "Michroma", Arial, sans-serif; color: var(--white);
    font-size: 27px; line-height: 1; letter-spacing: .5px;
  }
  .company-sub {
    font-family: "Michroma", Arial, sans-serif; color: var(--white);
    font-size: 10.5px; margin-top: 6px; letter-spacing: .6px;
  }
  .person-name {
    margin-top: 44px; color: var(--brand-green);
    font-size: 24px; font-weight: 400; letter-spacing: .5px; text-transform: uppercase;
  }
  .person-role { color: var(--white); font-size: 15px; margin-top: 2px; }
  .contact-list { list-style: none; margin-top: 10px; }
  .contact-list li {
    display: flex; align-items: center; gap: 10px;
    color: var(--muted); font-size: 14.5px; line-height: 23px;
  }
  .contact-list svg { width: 16px; height: 16px; flex: none; }
  .follow {
    display: flex; align-items: center; gap: 10px;
    margin-top: 10px; color: var(--white); font-size: 14.5px;
  }
  .follow .dot { width: 16px; height: 16px; border-radius: 50%; background: var(--brand-green); }
</style>
</head>
<body>
<main class="canvas">

  <section class="card card-back">
    <div class="pattern-field" role="img" aria-label="Subtle tonal repeat of the company mark across the card back"></div>
    <div class="brand-tag"><span class="brand-square"></span>KEYSTONE</div>
    <ul class="services">
      <li><span class="bullet">•</span>New Homes<span class="bullet">•</span>Extensions<span class="bullet">•</span>Renovations &amp; Bathrooms</li>
      <li><span class="bullet">•</span>Decking<span class="bullet">•</span>Carports<span class="bullet">•</span>Sheds (Residential and Industrial)</li>
      <li><span class="bullet">•</span>Carpentry<span class="bullet">•</span>Fences<span class="bullet">•</span>Patios &amp; Pergolas</li>
    </ul>
  </section>

  <section class="card card-front">
    <div class="front-mark" role="img" aria-label="Large green and grey brand mark panel"></div>
    <div class="front-content">
      <h1 class="company-name">KEYSTONE HOMES</h1>
      <p class="company-sub">AND DEVELOPMENTS PTY LTD</p>
      <h2 class="person-name">Daniel Harper</h2>
      <p class="person-role">Managing Director</p>
      <ul class="contact-list">
        <li>
          <svg viewBox="0 0 16 16" aria-hidden="true"><path fill="#33b54d" d="M3.5 1.5l2.5 0 1 3.5-1.6 1.2a8 8 0 0 0 4.4 4.4l1.2-1.6 3.5 1v2.5c0 .8-.7 1.5-1.5 1.5C6.6 14 2 9.4 2 3c0-.8.7-1.5 1.5-1.5z"/></svg>
          044-987 654 321
        </li>
        <li>
          <svg viewBox="0 0 16 16" aria-hidden="true"><rect x="1" y="3" width="14" height="10" rx="1" fill="#33b54d"/><path d="M1.5 3.8L8 9l6.5-5.2" fill="none" stroke="#0b0b0b" stroke-width="1.2"/></svg>
          info@keystonebuild.com
        </li>
        <li>
          <svg viewBox="0 0 16 16" aria-hidden="true"><circle cx="8" cy="8" r="7" fill="none" stroke="#33b54d" stroke-width="1.6"/><ellipse cx="8" cy="8" rx="3" ry="7" fill="none" stroke="#33b54d" stroke-width="1.2"/><path d="M1 8h14" stroke="#33b54d" stroke-width="1.2"/></svg>
          www.keystonebuild.com
        </li>
      </ul>
      <p class="follow">Follow us <span class="dot"></span></p>
    </div>
  </section>

</main>
</body>
</html>
```